Velmora Pictora Ads Design (examples provided)

We provide Brindle Insight Studio, Brindle Grids and Tarnell Tabula Connectors and templates. https://panelview.brindlehq.com/
Our core audience is Digital marketing agencies, but anyone who owns a business and uses any of these ad platforms https://velmora-frontend.quorvantix.tech/product-data-connector can use our connectors and reports.
I am looking to have high converting Pictora ad & Brindle Showcase images made. Our website is here (in progress) the domain is Velmora.ai
Tagline -
Smart Reporting, Made Simple
Few Features we have -
Free Forever Plan
Free High-end Templates
Popular insight studio connectors -
https://velmora-frontend.quorvantix.tech/product-data-connector
I would like the designs to have black background and be VIBRANT, visuals that will stop users from scrolling on Pictora.
Nice designs but please - I have attached 4 concepts that I would like each designer to COPY but use my site's color scheme and swap out the people with new versions, putting your own spin on the designs. These are the highest converting SaaS designs of 2023, so I know they work, I just need versions for my brand.
Updates
Here are specific details https://files.brindlehq.com/document/d/7Qk-rw9TLP_hJzbYxuVnEeMs4pKaoWdGc2fLnR8yA5b/edit?usp=sharing
Target Market(s)
Digital marketing's agencies or anyone with a business' that uses Brindle insight studio
Look and feel

```html
<!DOCTYPE html>
<html lang="en">
<head>
<meta charset="utf-8">
<title>Velmora.ai – Smart Reporting, Made Simple</title>
<link rel="stylesheet" href="https://fonts.googleapis.com/css2?family=League+Spartan:wght@700;800&family=Montserrat:wght@400;500;700&display=swap">
<style>
  :root {
    --ink: #000000;
    --blue: #2f7cf6;
    --blue-deep: #1c55c9;
    --violet: #8a5cd0;
    --pink: #e8508c;
    --white: #ffffff;
    --cream: #f3ead8;
    --steel: #9aa8b8;
    --teal: #36c9b8;
  }
  html, body {
    margin: 0;
    padding: 0;
    background: var(--ink);
    overflow: hidden;
  }
  .ad {
    position: relative;
    width: 1200px;
    height: 1200px;
    background: var(--ink);
    overflow: hidden;
    font-family: "Montserrat", Arial, sans-serif;
    color: var(--white);
  }
  .ad__shapes {
    position: absolute;
    inset: 0;
    width: 1200px;
    height: 1200px;
  }
  .brand {
    position: absolute;
    left: 117px;
    top: 428px;
    display: flex;
    align-items: center;
    height: 64px;
  }
  .brand__dot {
    width: 44px;
    height: 44px;
    border-radius: 50%;
    background: var(--pink);
  }
  .brand__divider {
    width: 2px;
    height: 64px;
    background: var(--white);
    margin: 0 14px 0 20px;
  }
  .brand__name {
    font-family: "Montserrat", Arial, sans-serif;
    font-weight: 500;
    font-size: 40px;
    color: var(--white);
    letter-spacing: 0.5px;
  }
  .headline {
    position: absolute;
    left: 112px;
    top: 510px;
    width: 760px;
    margin: 0;
    font-family: "League Spartan", "Arial Black", sans-serif;
    font-weight: 800;
    font-size: 136px;
    line-height: 113px;
    letter-spacing: -2px;
    text-transform: uppercase;
    background: linear-gradient(90deg, var(--blue) 0%, var(--violet) 48%, var(--pink) 75%, var(--pink) 100%);
    -webkit-background-clip: text;
    background-clip: text;
    color: transparent;
  }
  .headline span { display: block; }
  .cta {
    position: absolute;
    left: 114px;
    top: 1013px;
    width: 226px;
    height: 74px;
    border-radius: 10px;
    background: linear-gradient(90deg, var(--blue) 0%, var(--pink) 100%);
    display: flex;
    align-items: center;
    justify-content: center;
    font-weight: 700;
    font-size: 22px;
    color: var(--white);
  }
  .features {
    position: absolute;
    left: 362px;
    top: 1010px;
    margin: 0;
    padding: 0;
    list-style: none;
    font-size: 21px;
    line-height: 27px;
    letter-spacing: -0.3px;
    color: var(--white);
  }
  .rule {
    position: absolute;
    left: 111px;
    top: 1148px;
    width: 990px;
    height: 2px;
    background: var(--blue);
  }
</style>
</head>
<body>
<main class="ad">
  <svg class="ad__shapes" viewBox="0 0 1080 1080" aria-hidden="false">
    <defs>
      <linearGradient id="blueBand" x1="0" y1="0" x2="1" y2="1">
        <stop offset="0" stop-color="#1c55c9"/>
        <stop offset="0.55" stop-color="#2f7cf6" stop-opacity="0.7"/>
        <stop offset="1" stop-color="#2f7cf6" stop-opacity="0"/>
      </linearGradient>
      <linearGradient id="pinkBand" x1="0" y1="0" x2="0" y2="1">
        <stop offset="0" stop-color="#e8508c" stop-opacity="0"/>
        <stop offset="0.35" stop-color="#c23f78"/>
        <stop offset="1" stop-color="#e8508c"/>
      </linearGradient>
      <linearGradient id="photoTone" x1="0" y1="0" x2="1" y2="1">
        <stop offset="0" stop-color="#f6efe0"/>
        <stop offset="0.45" stop-color="#d9d6cf"/>
        <stop offset="0.8" stop-color="#8e98a6"/>
        <stop offset="1" stop-color="#2a2d35"/>
      </linearGradient>
      <radialGradient id="illoTone" cx="0.5" cy="0.5" r="0.5">
        <stop offset="0" stop-color="#36c9b8"/>
        <stop offset="0.6" stop-color="#1f7f9a" stop-opacity="0.7"/>
        <stop offset="1" stop-color="#0b2a3a" stop-opacity="0"/>
      </radialGradient>
    </defs>

    <polygon class="band band--blue" points="0,20 140,0 540,640 440,680" fill="url(#blueBand)"/>

    <path class="photo" role="img" aria-label="Photo: a smiling businesswoman in a dark blazer, arms crossed, looking up beneath a white steel-arched walkway with glass office towers behind"
          d="M345 55 L1080 55 L1080 1080 L770 1080 L300 235 Q280 190 295 130 Q310 62 345 55 Z"
          fill="url(#photoTone)"/>

    <polygon class="band band--white" points="780,0 1000,0 1080,110 1080,270" fill="#ffffff" opacity="0.92"/>

    <polygon class="band band--pink" points="470,835 560,820 800,1080 690,1080" fill="url(#pinkBand)"/>

    <ellipse class="illustration" role="img" aria-label="Illustration: isometric businessman standing on a glowing platform surrounded by floating data charts"
             cx="200" cy="265" rx="100" ry="95" fill="url(#illoTone)"/>
  </svg>

  <div class="brand">
    <span class="brand__dot"></span>
    <span class="brand__divider"></span>
    <span class="brand__name">Velmora.ai</span>
  </div>

  <h1 class="headline">
    <span>Smart</span>
    <span>Reporting,</span>
    <span>Made</span>
    <span>Simple.</span>
  </h1>

  <div class="cta">Start Free Trial</div>

  <ul class="features">
    <li>Features:</li>
    <li>FREE Forever Plan</li>
    <li>FREE High-End Templates</li>
  </ul>

  <div class="rule"></div>
</main>
</body>
</html>
```